Sassy Funky Web Design Project

NOTE: PAYMENT IS GUARANTEED for this project :)

++++++++++++++++++

I meant to share with you my mission for Caring Summit:

To inspire nurses to take action that impacts change in their lives, their organizations, or even the world.

Values:
I – Integrity
M – Mentoring / Motivation
P – Passion for excellence
A – Accountability
C – Competence / knowledge/ achievement
T – Transformation – positive change

++++++++++++++++++

This is a Membership site so will need to show 'Members Login' etc.

Please make sure you use SUPER HIGH QUALITY PHOTOGRAPHY / IMAGES :)

This is a WORDPRESS site for my client - here's some questions I asked her with her answers:

1. Why do you want a website (or have your current site redesigned)?

I want a website to generate income, and residual income, promote quality education material to professionals that is not the same on-line programs point and click to answer questions. I want an interactive way to make a impact in nursing hence CaringSUMMIT.

2. What’s your business/organization all about?

My parent company is Verity Brook Partners, LLC. I started it in 2001 and I provide consultative services to the legal and medical professionals. Mostly legal professionals; attorneys, and offer expert witness testimony. I also present full-day seminars regarding legal aspects of healthcare for nurses and hospital executive leaders. I am always promoting the professionalism in nursing where ever I can.

3. What sets your business apart from your competition?

What I will offer is instant access to quality and reliable clinical information and reliable business support for legal nurse consultants. I have not found another website that offers videos of clinical skills that nurses can watch over and over again without paying a lot of money for. Most of the information for nurses is through online learning read a packet, answer questions, and hopefully, maybe, they learned something. One of the reasons why my seminars are so well attended is they are interactive, and I use real examples to act out scenarios. I want nurses to be able to access short 7-10 minute video/podcasts that will show them how things are done and not just reading about it. Assessment skills will be performed on my family members in a clinic setting to create a realistic view. I want these to be somehow interactive if possible to reinforce the learning. Maybe you have some ideas on that.

For the legal nurse consultants. The programs are driving the “certification” outcome. When the nurses complete these programs, they have no experience and therefore are not able to recover their investment. I want to provide for them the same type of visual education support as the clinical nurses. These two audiences do not have to be mutually exclusive because they do tend to overlap in the real world.

I provide personal mentoring for novice legal nurse consultants in one week programs to support the application need in the LNC community. These weeks are valuable to the novice LNC trying to get started.

4. What problems does your business solve?

Application of concepts which is where I came up with Verity Brook Partners. I also have a tag with CaringSUMMIT I have used: Education, training, application. I put the theory into practice. I translate the pages to the living people.

5. Who are your prospective customers or visitors?

Customers:
Nurses, Advanced Practice Nurses, Legal Nurse Consultants, Attorneys for the clinical/medical information, Universities that offer nursing programs,
Nursing students (I really want to pursue this niche, perhaps a discount for enrolled students???)

Visitors:
Hospital Chief Nursing Officers, Attorneys, Long Term Care Administrators, Faculty of Nursing programs.

6. What do you NOT want on your website?

A flat appearing, boxy, traditional site. I want the nurses to be able to navigate through without much effort, remember many are technologically challenged….
NOooo cartoons… not too many stock photos, I would rather take real images if at all possible to keep the site “alive and real”.

What do you like?

QRV.tv: the listing of videos is going to be important in my site because I will be making clinical example videos and interview videos that can be viewed over and over again by the Platinum members. I plan to have a blog and many downloads available as well.

Tovamesh.com: I like the layout but I do want more interaction with mine. I do like the are you a training leader? Department leader: emerging leader? Componenets because I am addressing Nurses, Nurse Leaders, Legal Nurse Consultants… this would be important to establish right up front. I particularly like the video enhanced special report the new prospect has access to. I will do this for my site. I think it is also cool that you can change the color of the landing page to your liking.

www.thebrindlecove.com: I like a lot of things on this website but it is a bit difficult to navigate for even me. I like the short one minute capture of audio cds. I do plan to have CD material available. I do like the what you get with each level of membership under brindlelink tab. Some of the pages are not easy to read because the color is too dark and the font color is not contrasted enough. I like the tips in ten downloads on CD as well. I can see this working with mine as similar formatting with of course difference content.

www.ginaforsby.org: I do like the section she has on photo gallery where I can post event that have taken place as I speak, and work one-on-one with nurses across the country. (not the fashion shoot ?).

www.7horizons.com: I love the rollover interaction, the eyes constantly moving to the movement across the site.
http://www.dorvesta.org/DorvestaMultimedia.aspx?VideoId=8830461729004&type=M Quick lane video using sketchpad is a cool idea.

www.pebblevault.com - nice and clean

11. Please give us a list of websites that you DON’T Like and Why you Don’t like them.

www.lurn.com: landing page is way too crowded, too many colors, I don’t know where to go for what I would be looking for. Font is too small with large amounts of content.

www.casewardhub.com: this site is way too busy and difficult to navigate however I do like the page titled: Memorable BRWP cases. I would use a page like this for memorable Caring Summit experiences that would encourage others and remember the great things nurses do.

www.wardskills.com: Do not like at all. Way to juvenile.

Colour Scheme:

The colors palette I like is…. I think you will get the general idea of the color scheme. I like the yellow on dark colors so it pops, make sense?

F7C40E
4819A9
2E1FAC
F7D80E
Updates

Payment is guaranteed for this project now! :)

Thank you

Target Market(s)

Customers: Nurses, Advanced Practice Nurses, Legal Nurse Consultants, Attorneys for the clinical/medical information, Universities that offer nursing

Values:
I – Integrity
A – Accountability

Industry/Entity Type

Healthcare

Requirements
Must have
• professional, clean, VERY HIGH QUALITY IMAGES/ PHOTOGRAPHY e.g. PixQuarry
Nice to have
• Brock:
I have shown the design template to several people to get their first impression. I was shocked. They thought of the Tacoma Riveters! The football team. Ouch. I don’t want that. Crazy what others see.
Can we please change the color scheme to incorporate the colors below with the same layout. The Layout is good, it is the color I need to work a bit more on. Sorry about this but I don’t want to be a Riveters fan.

336699
FFCC66
FFFFFF
003366

Yvonne

New logo required: Caring Summit - DO NOT USE MEDICAL
Should not have
• childish graphics, or icons.
Don't want to see unprofessional site with clumsy type or template type designs. We can include some photos.

```html
<!DOCTYPE html>
<html lang="en">
<head>
<meta charset="utf-8">
<title>Verity Brook Partners, LLC — Caring Summit Training</title>
<link rel="stylesheet" href="https://fonts.googleapis.com/css2?family=PT+Serif:wght@400;700&family=Open+Sans:wght@400;600;700&family=Cinzel:wght@400;700&display=swap">
<style>
:root{
  --green-deep:#0d4337;
  --green:#175847;
  --green-soft:#1f6a56;
  --yellow:#f7c40e;
  --yellow-soft:#f7d46a;
  --blue:#2e1fac;
  --purple:#4819a9;
  --lavender:#dcd6f7;
  --ink:#2b2b2b;
  --muted:#7a7a7a;
  --line:#e3e3e3;
  --white:#ffffff;
}
*{margin:0;padding:0;box-sizing:border-box}
html,body{width:1200px;height:2250px;overflow:hidden}
body{position:relative;background:var(--white);font-family:"Open Sans",Arial,sans-serif;color:var(--ink);font-size:13px}
.abs{position:absolute}
h2,h3{font-family:"PT Serif",Georgia,serif;font-weight:400;color:#222}

/* header */
.site-header{left:0;top:0;width:1200px;height:718px;background:linear-gradient(180deg,var(--green-deep) 0,var(--green) 110px,var(--green) 100%)}
.util-bar{left:800px;top:0;width:312px;height:35px;background:var(--yellow);display:flex;align-items:center;font-size:12px;color:#4a3b00}
.util-bar .member{padding:0 14px 0 16px;border-right:1px solid rgba(0,0,0,.2)}
.util-bar .phone{padding-left:14px;display:flex;align-items:center;gap:6px}
.brand{left:95px;top:14px;display:flex;align-items:center;gap:12px;color:var(--white);font-family:"PT Serif",Georgia,serif;font-size:19px;letter-spacing:.5px}
.brand .mark{width:40px;height:40px;border:2px solid var(--white)}
.main-nav{left:565px;top:56px;display:flex;gap:6px;font-size:13px;font-weight:600}
.main-nav a{color:var(--yellow);text-decoration:none;padding:6px 12px;border-radius:3px}
.main-nav a.current{background:#d9d9d9;color:#333}
.hero{left:88px;top:132px;width:1024px;height:543px;border-radius:4px;background:linear-gradient(135deg,#a9b8c2 0%,#7fb7cf 35%,#4aa9c8 60%,#8aa6b5 100%)}
.hero-caption{left:638px;top:512px;width:474px;height:80px;background:rgba(12,60,48,.85);padding:10px 16px}
.hero-caption .title{font-family:"Cinzel",Georgia,serif;font-size:28px;color:var(--white);font-weight:700;line-height:1.1}
.hero-caption .title span{color:var(--yellow)}
.hero-caption .sub{font-size:12px;color:#d6e6df;margin-top:4px}
.hero-dots{left:555px;top:686px;display:flex;gap:10px}
.hero-dots i{width:10px;height:10px;border-radius:50%;background:var(--yellow);display:block}
.hero-dots i.on{background:#c79a00}

/* content */
.section-title{font-size:27px}
.welcome{left:88px;top:758px;width:637px}
.welcome .lead{color:var(--muted);font-size:12px;margin-top:4px}
.welcome p.body{margin-top:22px;font-size:13px;line-height:19.5px;color:#444}
.btn{display:inline-block;background:var(--blue);color:var(--white);font-size:12px;font-weight:600;padding:6px 14px;border-radius:3px}
.pager{display:flex;gap:6px}
.pager i{width:26px;height:26px;border-radius:50%;background:var(--green);display:flex;align-items:center;justify-content:center}
.video-box{left:798px;top:805px;width:314px;height:220px;background:linear-gradient(160deg,#2a2a2a,#555 55%,#1c1c1c)}

.news{left:88px;top:1062px;width:325px}
.news-item{display:flex;gap:12px;margin-top:22px}
.thumb{flex:none;width:62px;height:55px;background:linear-gradient(135deg,#6d7d70,#c3c8b2)}
.news-item h4{font-size:12.5px;font-weight:600;color:var(--blue)}
.meta{font-size:11px;color:var(--muted);margin:3px 0 8px}
.news-item p{font-size:12px;line-height:17px;color:#444}

.trainer{left:442px;top:1062px;width:308px}
.trainer-card{display:flex;gap:16px;margin-top:22px}
.trainer-photo{width:125px;height:150px;background:linear-gradient(160deg,#6a4a36,#b58a63 60%,#3d2a20)}
.trainer-info{font-size:11.5px;color:#555;flex:1}
.trainer-info div{padding:6px 0;border-bottom:1px solid var(--line)}
.trainer-info .name{font-weight:700;color:#222;font-size:12.5px;border:0;padding-bottom:0}
.trainer-info .role{color:var(--muted);padding-top:2px}
.trainer p{margin-top:28px;font-size:12px;line-height:18px;color:#444}

.programs{left:798px;top:1062px;width:314px}
.program-list{list-style:none;margin-top:14px}
.program-list li{display:flex;justify-content:space-between;align-items:center;height:37.5px;border-bottom:1px solid var(--line);font-size:12px;color:var(--blue)}
.star{width:26px;height:26px;border-radius:50%;background:var(--green);display:flex;align-items:center;justify-content:center}
.star.alt{background:var(--purple)}
.new-class{left:798px;top:1325px;width:314px;height:140px;background:var(--yellow-soft);padding:14px 20px}
.new-class h3{font-size:28px;color:var(--green)}
.new-class h3 b{font-family:"Open Sans",Arial,sans-serif;font-weight:700}
.new-class p{font-size:11px;color:#7a6a2a;line-height:15px;margin-top:4px}
.new-class .call{text-align:right;font-size:17px;color:var(--green);margin-top:8px}

.features{left:88px;top:1545px;width:680px;height:185px;background:var(--lavender)}
.feature{position:absolute;top:20px;width:130px;text-align:center;font-size:12px;color:#333}
.feature .circle{width:92px;height:92px;border-radius:50%;background:var(--white);margin:0 auto 10px;display:flex;align-items:center;justify-content:center}
.feature-dots{left:400px;top:155px;display:flex;gap:10px}
.feature-dots i{width:10px;height:10px;border-radius:50%;background:var(--blue);display:block}
.feature-dots i.on{background:var(--green)}
.facilities{left:798px;top:1538px;width:314px}
.facility-img{margin-top:12px;width:314px;height:142px;background:linear-gradient(180deg,#8a7c66,#5e6a7c 55%,#b7aa90)}

/* footer */
.site-footer{left:0;top:1832px;width:1200px;height:373px;background:var(--green)}
.site-footer h3{color:var(--white);font-size:25px}
.f-col{position:absolute;top:52px}
.entry,.tweet{display:flex;gap:14px;margin-top:22px}
.entry .thumb{width:62px;height:62px;background:linear-gradient(135deg,#555,#bbb)}
.entry h4{font-size:12.5px;color:var(--yellow);font-weight:600}
.entry .meta{color:#a9c7bc}
.entry p{font-size:11.5px;color:#d8e6e0;line-height:16px}
.tweet{font-size:11.5px;color:#d8e6e0;line-height:16px}
.tweet .dot{flex:none;width:22px;height:22px;border-radius:50%;background:var(--yellow);margin-top:4px}
.tweet a{color:var(--yellow);font-weight:600;text-decoration:none}
.field{display:block;width:224px;height:30px;background:var(--white);border:1px solid #ccc;margin-top:15px;font-size:11.5px;color:#999;padding:7px 8px}
.field.msg{width:307px;height:90px}
.submit{margin-top:15px;display:inline-block;background:var(--blue);color:var(--white);font-size:12px;padding:6px 12px;border-radius:2px}
.bottom-bar{left:0;top:2205px;width:1200px;height:45px;background:var(--green-deep);display:flex;align-items:center;justify-content:space-between;padding:0 88px;color:#cfe0d9;font-size:11.5px}
.social{display:flex;gap:8px}
.social i{width:24px;height:24px;border-radius:50%;display:block}
</style>
</head>
<body>

<header class="abs site-header">
  <div class="abs util-bar">
    <span class="member">Register » Login » Download</span>
    <span class="phone">
      <svg width="12" height="12" viewBox="0 0 24 24"><path d="M6.6 10.8a15 15 0 0 0 6.6 6.6l2.2-2.2a1 1 0 0 1 1-.25 11.4 11.4 0 0 0 3.6.57 1 1 0 0 1 1 1V20a1 1 0 0 1-1 1A17 17 0 0 1 3 4a1 1 0 0 1 1-1h3.5a1 1 0 0 1 1 1c0 1.25.2 2.45.57 3.57a1 1 0 0 1-.25 1z" fill="#4a3b00"/></svg>
      +212 555 0148
    </span>
  </div>
  <div class="abs brand"><span class="mark"></span>Verity Brook Partners, LLC</div>
  <nav class="abs main-nav">
    <a class="current">Home</a><a>Training</a><a>Features</a><a>Facilities</a><a>Lectures</a><a>Videos</a><a>Contact</a>
  </nav>
  <div class="abs hero" role="img" aria-label="Photo of four smiling nurses in scrubs in a hospital ward"></div>
  <div class="abs hero-caption">
    <div class="title">CARING <span>SUMMIT TRAINING</span></div>
    <div class="sub">Reliable business support for legal nurse consultants training 2012</div>
  </div>
  <div class="abs hero-dots"><i></i><i class="on"></i><i></i><i></i></div>
</header>

<section class="abs welcome">
  <h2 class="section-title">Welcome to Verity Brook Partners, LLC</h2>
  <div class="lead">started it in 2001 and I provide consultative services to the legal and medical professionals</div>
  <p class="body">Full-day seminars regarding legal aspects of healthcare for nurses and hospital executive leaders.<br>
  I am always promoting the professionalism in nursing where ever I can. When the nurses complete<br>
  these programs, they have no experience and therefore are not able to recover their investment.<br>
  I want to provide for them the same type of visual education support as the clinical nurses.<br>
  I provide personal mentoring for novice legal nurse consultants in one week programs.</p>
  <span class="btn" style="margin-top:14px">Read more</span>
</section>

<div class="abs" style="left:798px;top:768px;width:314px;display:flex;justify-content:space-between;align-items:center">
  <h2 class="section-title" style="font-size:25px">Training Videos</h2>
  <div class="pager">
    <i><svg width="10" height="10" viewBox="0 0 10 10"><path d="M7 1 3 5l4 4" stroke="#fff" stroke-width="1.8" fill="none"/></svg></i>
    <i><svg width="10" height="10" viewBox="0 0 10 10"><path d="M3 1l4 4-4 4" stroke="#fff" stroke-width="1.8" fill="none"/></svg></i>
  </div>
</div>
<div class="abs video-box" role="img" aria-label="Video still of a clinical training session">
  <svg class="abs" style="left:127px;top:80px" width="60" height="60" viewBox="0 0 60 60"><circle cx="30" cy="30" r="28" fill="rgba(0,0,0,.55)"/><path d="M24 18l18 12-18 12z" fill="#ddd"/></svg>
</div>

<section class="abs news">
  <h2 class="section-title" style="font-size:25px">Training News &amp; Events</h2>
  <div class="news-item"><div class="thumb" role="img" aria-label="Operating room photo"></div><div>
    <h4>Operating Room Training Program</h4><div class="meta">23 Jul 2012 :: Verity LLC</div>
    <p>Presents a unique opportunity to work in a highly specialized environment</p></div></div>
  <div class="news-item" style="margin-top:30px"><div class="thumb" role="img" aria-label="Nursing students photo"></div><div>
    <h4>Fulfilling nursing career choice</h4><div class="meta">13 Jul 2012 :: Verity LLC</div>
    <p>It prepares the practical nurse (PN) candidate to become qualified</p></div></div>
  <div class="news-item" style="margin-top:30px"><div class="thumb" role="img" aria-label="Counseling session photo"></div><div>
    <h4>Health and Counseling Services</h4><div class="meta">05 Jul 2012 :: Verity LLC</div>
    <p>As with all students, health and counseling services are provided</p></div></div>
</section>

<section class="abs trainer">
  <h2 class="section-title" style="font-size:25px">Featured Trainers</h2>
  <div class="trainer-card">
    <div class="trainer-photo" role="img" aria-label="Portrait of a featured nurse trainer"></div>
    <div class="trainer-info">
      <div class="name">Your name here</div>
      <div class="role">Nurse lecture</div>
      <div>contact@veritybrook.com</div>
      <div>+62-555-01234</div>
      <div style="border:0">08 am to 3 pm</div>
    </div>
  </div>
  <p>Practical nurses are valuable both in the care of the sick and in providing health instruction to the patient as well, noted for their good bedside manners; they are calm, positive, cheerful, comforting, compassionate, kind, and pleasant</p>
  <span class="btn" style="margin-top:14px">Read more</span>
</section>

<section class="abs programs">
  <h2 class="section-title" style="font-size:25px">Training programs</h2>
  <ul class="program-list">
    <li>Operating Room Training Program<span class="star"><svg width="14" height="14" viewBox="0 0 24 24"><path d="M12 2l3 7h7l-5.5 4.5 2 7.5L12 17l-6.5 4 2-7.5L2 9h7z" fill="#f7c40e"/></svg></span></li>
    <li>Learning opportunities<span class="star"><svg width="14" height="14" viewBox="0 0 24 24"><path d="M12 2l3 7h7l-5.5 4.5 2 7.5L12 17l-6.5 4 2-7.5L2 9h7z" fill="#f7c40e"/></svg></span></li>
    <li>Education and Diploma<span class="star alt"><svg width="14" height="14" viewBox="0 0 24 24"><path d="M12 2l3 7h7l-5.5 4.5 2 7.5L12 17l-6.5 4 2-7.5L2 9h7z" fill="#fff"/></svg></span></li>
    <li>Nursing Assistant Theory<span class="star"><svg width="14" height="14" viewBox="0 0 24 24"><path d="M12 2l3 7h7l-5.5 4.5 2 7.5L12 17l-6.5 4 2-7.5L2 9h7z" fill="#f7c40e"/></svg></span></li>
    <li>Medical Terminology Program<span class="star"><svg width="14" height="14" viewBox="0 0 24 24"><path d="M12 2l3 7h7l-5.5 4.5 2 7.5L12 17l-6.5 4 2-7.5L2 9h7z" fill="#f7c40e"/></svg></span></li>
  </ul>
</section>

<aside class="abs new-class">
  <h3>New class <b>available</b></h3>
  <p>Successful completion of this course will allow the student to utilize and translate medical</p>
  <div class="call">Call Us &nbsp;<b>+212 555 0199</b></div>
</aside>

<section class="abs features">
  <div class="feature" style="left:9px"><div class="circle"><svg width="40" height="40" viewBox="0 0 40 40"><circle cx="20" cy="16" r="10" fill="none" stroke="#175847" stroke-width="3"/><path d="M14 25l-3 12 9-4 9 4-3-12" fill="#175847"/></svg></div>Benefits Programs</div>
  <div class="feature" style="left:142px"><div class="circle"><svg width="40" height="40" viewBox="0 0 40 40"><rect x="8" y="6" width="24" height="30" rx="2" fill="none" stroke="#175847" stroke-width="3"/><path d="M13 15h14M13 21h14M13 27h9" stroke="#175847" stroke-width="3"/></svg></div>Register Online</div>
  <div class="feature" style="left:272px"><div class="circle"><svg width="40" height="40" viewBox="0 0 40 40"><g fill="#175847"><circle cx="9" cy="11" r="3"/><circle cx="9" cy="20" r="3"/><circle cx="9" cy="29" r="3"/><rect x="15" y="9" width="18" height="4"/><rect x="15" y="18" width="18" height="4"/><rect x="15" y="27" width="18" height="4"/></g></svg></div>Current students</div>
  <div class="feature" style="left:402px"><div class="circle"><svg width="40" height="40" viewBox="0 0 40 40"><path d="M6 9h12v24H6zM22 9h12v24H22z" fill="none" stroke="#175847" stroke-width="3"/></svg></div>Community</div>
  <div class="feature" style="left:539px"><div class="circle"><svg width="40" height="40" viewBox="0 0 40 40"><g fill="#175847"><circle cx="14" cy="13" r="5"/><circle cx="27" cy="13" r="5"/><path d="M4 32c0-7 5-11 10-11s10 4 10 11zM18 32c1-7 5-11 9-11s9 4 9 11z"/></g></svg></div>Professional dev.</div>
  <div class="abs feature-dots"><i class="on"></i><i></i><i class="on"></i></div>
</section>

<section class="abs facilities">
  <div style="display:flex;justify-content:space-between;align-items:center">
    <h2 class="section-title" style="font-size:25px">Training Facilities</h2>
    <div class="pager">
      <i><svg width="10" height="10" viewBox="0 0 10 10"><path d="M7 1 3 5l4 4" stroke="#fff" stroke-width="1.8" fill="none"/></svg></i>
      <i><svg width="10" height="10" viewBox="0 0 10 10"><path d="M3 1l4 4-4 4" stroke="#fff" stroke-width="1.8" fill="none"/></svg></i>
    </div>
  </div>
  <div class="facility-img" role="img" aria-label="Photo of a seminar room set with tables and chairs"></div>
</section>

<footer class="abs site-footer">
  <div class="f-col" style="left:88px;width:320px">
    <h3>Recent Entries</h3>
    <div class="entry"><div class="thumb" role="img" aria-label="Blog entry photo"></div><div>
      <h4>Verity Media just lorem ipsum</h4><div class="meta">11 Apr 2012 :: Verity Media</div>
      <p>Lorem ipsum dolor sit amet, Lorem ipsum dolor sit amet, ...</p></div></div>
    <div class="entry" style="margin-top:26px"><div class="thumb" role="img" aria-label="Blog entry photo"></div><div>
      <h4>Verity Media open new program at</h4><div class="meta">03 Apr 2012 :: Verity Media</div>
      <p>Lorem ipsum dolor sit amet, Lorem ipsum dolor sit amet, ...</p></div></div>
  </div>
  <div class="f-col" style="left:442px;width:320px">
    <h3>Latest Tweets</h3>
    <div class="tweet"><span class="dot"></span><div>Verity LLC just say hello on #tweet<br>'Nurse program professional '<br><a>http://t.co/vbrook</a> 1weeks ago</div></div>
    <div class="tweet"><span class="dot"></span><div>Verity LLC just say hello on #tweet<br>'Nurse program videos'<br><a>http://t.co/vbrook</a> 2weeks ago</div></div>
    <div class="tweet"><span class="dot"></span><div>Verity LLC just say hello on #tweet<br>'Nurse program '</div></div>
  </div>
  <div class="f-col" style="left:798px;width:320px">
    <h3>Contact Us</h3>
    <span class="field" style="margin-top:20px">Name</span>
    <span class="field">Email Address</span>
    <span class="field msg">Message</span>
    <span class="submit">Submit</span>
  </div>
</footer>

<div class="abs bottom-bar">
  <span>Copyright 2012, All rights Reserved. Verity Brook Training Programs</span>
  <div class="social"><i style="background:#3fa9d6"></i><i style="background:#3b5a9a"></i><i style="background:#555"></i><i style="background:#e8731c"></i></div>
</div>

</body>
</html>
```